Business Intelligence/Analytics Technology Company Business Card

We are a higher-end enterprise software development company working with Retailer POS data to provide business intelligence and analytical services to fortune 500 companies.

I have an immediate need for a professional/thick/bold business card. The same design aspects will spiral into more media such as flyers/folders/etc...

Our website is www.kovenmrx.com for our product.

I like "Clean" designs if that makes sense, not a lot of "stuff".

The uploaded files, the A logo with the box is the style we're leaning towards, but the A logo without the blue box is all good too... get creative.

Target Market(s)

Executives of large companies, down to VP level..

Industry/Entity Type

Software

Requirements
Must have
• I'm wanting a thick designer like business card.

I think we're going to change our logo to a more lumora 6 looking style... http://www.kovenmrx.com/card.ai as an example of our current business card.

The winner will also have knowledge of where i can get these things printed.
Nice to have
• Blue-ish color scheme? I'm open to anything. Our Competition is Red, and another is Green. So we'll stick with the Blue.

```html
<!DOCTYPE html>
<html lang="en">
<head>
<meta charset="utf-8">
<title>Koven Business Card</title>
<link rel="stylesheet" href="https://fonts.googleapis.com/css2?family=Montserrat:wght@300;400;600&display=swap">
<style>
  :root {
    --bg: #d9dadc;
    --blue-deep: #0b3f8f;
    --blue-mid: #1558b8;
    --blue-light: #2a7bd4;
    --white: #ffffff;
    --paper: #f3f4f7;
    --grey-text: #6d6f75;
    --pale-blue: #9cc3f0;
  }
  * { margin: 0; padding: 0; box-sizing: border-box; }
  html, body { width: 1200px; height: 900px; overflow: hidden; }
  body {
    background: var(--bg);
    font-family: "Montserrat", "Helvetica Neue", Arial, sans-serif;
    position: relative;
  }
  .card {
    position: absolute;
    left: 320px;
    width: 560px;
    height: 320px;
    border-radius: 6px;
    overflow: hidden;
    box-shadow: 0 10px 28px rgba(0,0,0,0.18);
  }
  /* Front */
  .card-front {
    top: 110px;
    background: linear-gradient(135deg, var(--blue-deep) 0%, var(--blue-mid) 55%, var(--blue-light) 100%);
    display: flex;
    flex-direction: column;
    align-items: center;
    justify-content: center;
    color: var(--white);
  }
  .front-brand {
    display: flex;
    align-items: center;
    gap: 22px;
  }
  .brand-square {
    width: 56px;
    height: 56px;
    background: var(--white);
  }
  .front-name {
    font-weight: 400;
    font-size: 78px;
    letter-spacing: 12px;
    line-height: 1;
  }
  .front-web {
    margin-top: 18px;
    font-weight: 300;
    font-size: 14px;
    letter-spacing: 2.5px;
    text-transform: uppercase;
    padding-left: 78px;
  }
  /* Back */
  .card-back {
    top: 490px;
    background: linear-gradient(180deg, var(--blue-mid) 0%, var(--blue-deep) 100%);
  }
  .back-head {
    position: absolute;
    top: 0; left: 0; right: 0;
    height: 150px;
    background: linear-gradient(90deg, var(--white) 0%, var(--paper) 100%);
  }
  .back-notch {
    position: absolute;
    left: 84px;
    top: 150px;
    width: 0; height: 0;
    border-left: 14px solid transparent;
    border-right: 14px solid transparent;
    border-top: 14px solid var(--white);
  }
  .back-brand {
    position: absolute;
    left: 56px;
    top: 46px;
    display: flex;
    align-items: center;
    gap: 16px;
  }
  .back-brand .brand-square {
    width: 40px; height: 40px;
    background: var(--blue-mid);
  }
  .back-name {
    font-weight: 400;
    font-size: 52px;
    letter-spacing: 8px;
    color: var(--grey-text);
    line-height: 1;
  }
  .back-tagline {
    position: absolute;
    left: 112px;
    top: 110px;
    font-size: 11px;
    letter-spacing: 2px;
    color: var(--blue-mid);
    text-transform: uppercase;
  }
  .contact {
    position: absolute;
    top: 186px;
    color: var(--white);
    font-weight: 300;
    font-size: 12.5px;
    letter-spacing: 1px;
    line-height: 1.55;
    text-transform: uppercase;
  }
  .contact-person { left: 56px; }
  .contact-office {
    left: 318px;
    padding-left: 18px;
    border-left: 1px solid rgba(255,255,255,0.45);
  }
  .person-name {
    font-weight: 600;
    font-size: 17px;
    letter-spacing: 1px;
  }
  .person-role { margin-bottom: 12px; }
  .label { color: var(--pale-blue); font-weight: 400; }
  .contact-email { text-transform: uppercase; }
</style>
</head>
<body>
  <section class="card card-front" aria-label="Card front">
    <div class="front-brand">
      <span class="brand-square"></span>
      <span class="front-name">KOVEN</span>
    </div>
    <p class="front-web">www.kovenmrx.com</p>
  </section>

  <section class="card card-back" aria-label="Card back">
    <div class="back-head"></div>
    <div class="back-notch"></div>
    <div class="back-brand">
      <span class="brand-square"></span>
      <span class="back-name">KOVEN</span>
    </div>
    <p class="back-tagline">Koven · Signal · Retail Health</p>

    <div class="contact contact-person">
      <p class="person-name">DANA WHITFIELD</p>
      <p class="person-role">Business Director</p>
      <p class="contact-email"><span class="label">E:</span> dana@kovenmrx.com</p>
      <p><span class="label">C:</span> 555.370.2286</p>
    </div>

    <div class="contact contact-office">
      <p>Koven Technology Group, Inc</p>
      <p>1450 Orrin Ave, Suite 210</p>
      <p>Fairhaven, AR 72901</p>
      <p style="margin-top:10px"><span class="label">P:</span> 555.210.4418</p>
      <p><span class="label">F:</span> 555.210.4419</p>
    </div>
  </section>
</body>
</html>
```